Website Design for new skincare product launch/rebranding

The Dew Harbor website is currently live and built through Pagelume.com. While the existing site has served as a strong starting point, I’m now looking to elevate the overall experience with a complete redesign that reflects the growth and vision of the brand. This will be a full visual and functional revamp — not just a refresh — with the goal of creating a more elevated, intuitive, and conversion-focused platform. I’m looking for a designer who can not only reimagine the layout and visuals, but also collaborate on optimizing the user journey and site structure for both storytelling and sales.

Target Market(s)

Age 25- 45 (core), with secondary appeal to 18-55. Primarily women, but gender inclusive. Wellness/Holistic Beauty/Organic Ingredients, Botanical.

Industry/Entity Type

Beauty, aesthetics, wellness.

Number of Pages Required

5+ page

Font styles to use
Other font styles liked:
• Thorvale Sans Family

Colors

Designer to choose colors to be used in the design.

Requirements
Must have
• Include standard pages (Home, Our Story/Values, Shop, Product Detail with ingredients/description/etc., Contact) and any other recommended sections to optimize conversion. Minimal, clean, calming visual. Seamlessly integrate with Vendara for all product sales.
Nice to have
• Company colors are attached in images, along with first two products that are launching. One called Lumivelt, and one called Serapoise. Fonts and shapes need to align accordingly. Feel elevated, neutral, and luxe while maintaining a grounded, earthy minimalism. Visual inspiration includes brands like Maple Tenet, Vessa Orlaine, and TOrveli — minimal yet high-end, with thoughtful use of whitespace, typography, and subtle movement. Would LOVE to have movement (short clip GIF) on either the home page or ingredient page, reference TOrveli website (homepage or LumaKnit Process™ Tab)
Should not have
• dark colors, complex design elements, too many different fonts. For ingredients, stick to botanical images and information only, with no mentions of CBD or use of leaf imagery.

```html
<!DOCTYPE html>
<html lang="en">
<head>
<meta charset="utf-8">
<title>Dew Harbor — Botanical Skincare</title>
<link href="https://fonts.googleapis.com/css2?family=Italiana&family=Poppins:wght@300;400;500&display=swap" rel="stylesheet">
<style>
:root{
  --ink:#1f1f1f;
  --muted:#6b6b6b;
  --accent:#9a9a92;
  --accent-soft:#b9b9b2;
  --paper:#ffffff;
  --mist:#f3f3f1;
  --line:#d9d9d6;
  --star:#f2b01e;
}
*{margin:0;padding:0;box-sizing:border-box}
html,body{width:1200px;height:4441px;overflow:hidden}
body{position:relative;background:var(--paper);color:var(--ink);font-family:"Poppins",sans-serif}
.abs{position:absolute}
.display{font-family:"Italiana",serif;font-weight:400;line-height:1.12;color:var(--ink)}
.btn{position:absolute;display:flex;align-items:center;justify-content:center;border-radius:30px;font-family:"Italiana",serif;font-size:15px}
.btn-fill{background:var(--accent);color:#fff}
.btn-line{background:#fff;color:var(--ink);border:1px solid var(--accent-soft)}
.photo{position:absolute}

/* hero */
.hero{position:absolute;left:0;top:0;width:1200px;height:606px;background:linear-gradient(100deg,#d9d5d0 0%,#e6e1db 40%,#d8cec4 62%,#bfb3a7 100%)}
.logo{position:absolute;font-family:"Italiana",serif;color:var(--ink)}
.nav-pill{position:absolute;left:530px;top:22px;width:373px;height:36px;background:#fff;border-radius:20px;display:flex;align-items:center;padding:0 16px;gap:16px;font-size:11px;color:var(--muted)}
.nav-pill .on{color:var(--ink)}
.nav-icons{margin-left:auto;display:flex;gap:5px}
.nav-icons span{width:15px;height:15px;border-radius:50%;background:var(--accent)}
.hero h1{position:absolute;left:150px;top:150px;font-size:64px;line-height:1.12}
.hero p{position:absolute;left:150px;top:378px;width:440px;font-size:14px;line-height:1.6}

/* feature */
.bullet{position:absolute;left:580px;width:460px;font-size:9.5px;line-height:1.6;color:var(--muted);padding-left:20px}
.bullet::before{content:"";position:absolute;left:2px;top:4px;width:9px;height:9px;border-radius:50%;background:var(--line)}
.bullet b{color:var(--ink);font-weight:500}

/* story */
.story{position:absolute;left:0;top:1760px;width:1200px;height:562px;background:var(--mist)}
.stat{position:absolute;top:2108px;font-size:10.5px;line-height:1.6;color:var(--muted)}
.stat strong{display:block;font-family:"Italiana",serif;font-weight:400;font-size:30px;color:var(--accent);line-height:1.1}

/* values */
.value{position:absolute;top:2500px;width:160px;text-align:center;font-size:14px}
.value svg{display:block;margin:0 auto 22px}

/* shop */
.card-img{position:absolute;top:2883px;width:366px;height:370px;border-radius:40px 40px 0 0;background:linear-gradient(180deg,#ddd6d1 0%,#f1eeeb 70%,#fff 100%)}
.card-name{position:absolute;top:3290px;font-size:14px;letter-spacing:.3px}
.card-desc{position:absolute;top:3322px;width:366px;font-size:11.5px;line-height:1.7;color:var(--muted)}
.price{position:absolute;top:3372px;font-size:17px}
.price s{font-size:11px;color:var(--muted);margin-left:6px}
.stars{position:absolute;top:3374px;color:var(--star);font-size:14px;letter-spacing:1px}
.cart{position:absolute;top:3415px;width:44px;height:37px;border:1px solid var(--accent-soft);border-radius:8px;display:flex;align-items:center;justify-content:center}

/* testimonials */
.quote{position:absolute;top:3693px;width:183px;height:267px;background:linear-gradient(180deg,#fff,#f7f7f5);padding:20px 14px}
.quote.featured{background:var(--accent);color:#fff}
.quote .mark{font-family:"Italiana",serif;font-size:30px;line-height:.6;color:var(--accent)}
.quote.featured .mark{color:#fff}
.quote p{font-size:8.5px;line-height:1.55;text-align:center;color:var(--muted);margin-top:6px}
.quote.featured p{color:#f3f3f3}
.quote .end{text-align:right;margin-top:4px}
.who{position:absolute;left:26px;bottom:26px;display:flex;align-items:center;gap:8px;font-size:10.5px;letter-spacing:.5px;color:var(--muted)}
.quote.featured .who{color:#fff}
.avatar{width:34px;height:34px;border-radius:50%;background:linear-gradient(135deg,#6e625a,#c9bdb1)}

/* footer */
.footer{position:absolute;left:0;top:4052px;width:1200px;height:389px;background:var(--mist)}
.foot-col{position:absolute;top:4188px;font-size:10.5px;line-height:1}
.foot-col h4{font-weight:400;font-size:11.5px;margin-bottom:16px}
.foot-col li{list-style:none;color:var(--muted);font-size:9.5px;margin-bottom:18px;display:flex;gap:10px;align-items:center}
.social{position:absolute;top:4274px;width:22px;height:22px;border-radius:50%;background:#fff;border:1px solid var(--line)}
</style>
</head>
<body>

<!-- HERO -->
<section class="hero">
  <div class="photo" role="img" aria-label="Woman applying a dropper serum to her cheek in a soft bright bathroom" style="left:560px;top:0;width:640px;height:606px;background:radial-gradient(ellipse at 60% 45%,#e9d3c2 0%,#d4c0b0 35%,rgba(200,188,176,0) 70%)"></div>
  <div class="logo" style="left:150px;top:24px;font-size:19px;letter-spacing:.5px">DEW HARBOR</div>
  <nav class="nav-pill">
    <span class="on">Home</span><span>Our Story</span><span>Shop ⌄</span><span>FAQ</span><span>Blog</span>
    <div class="nav-icons"><span></span><span></span><span></span><span></span></div>
  </nav>
  <a class="btn btn-fill" style="left:925px;top:22px;width:118px;height:36px">Contact Us</a>
  <h1 class="display">Align Your Skin<br>With Nature’s<br>Intelligence</h1>
  <p>Minimal, Botanical, And Scientifically Crafted Skincare For Radiant, Balanced Skin.</p>
  <a class="btn btn-fill" style="left:150px;top:468px;width:112px;height:38px">Shop Now</a>
  <a class="btn btn-line" style="left:284px;top:468px;width:178px;height:38px">Discover Our Story</a>
</section>

<!-- FEATURE -->
<section>
  <div class="photo" role="img" aria-label="Serapoise botanical balm jar beside a grey Lumivelt serum dropper bottle" style="left:145px;top:700px;width:395px;height:460px;background:radial-gradient(ellipse at 40% 50%,#efefed 0%,#e2e2df 40%,#fff 72%)"></div>
  <h2 class="display abs" style="left:580px;top:712px;font-size:56px">Grow Faster.<br>Smarter. Better.</h2>
  <p class="bullet" style="top:865px"><b>Lumivelt :</b> A weightless gel serum that floods skin with moisture and leaves a soft glass-like finish all day.</p>
  <p class="bullet" style="top:910px"><b>Serapoise :</b> A rich botanical balm that restores the barrier and calms dryness. Gentle enough for daily use.</p>
  <h3 class="display abs" style="left:580px;top:982px;font-size:35px;line-height:1.15">Pure Perfection<br>Naturally</h3>
  <div class="abs" style="left:580px;top:1096px;font-size:19px;font-weight:500"><sup style="font-size:10px">$</sup>23,99</div>
  <a class="btn btn-fill" style="left:707px;top:1092px;width:120px;height:36px">Buy It Now</a>
  <div class="photo" role="img" aria-label="Close-up of a cheek with a dab of white cream" style="left:843px;top:990px;width:210px;height:140px;border-radius:14px;background:linear-gradient(110deg,#dde3e6 0%,#eedcd0 55%,#e6c9b8 100%)"></div>
</section>

<!-- BOTANICALS -->
<section>
  <h2 class="display abs" style="left:150px;top:1238px;font-size:56px">The Power<br>Of Botanicals</h2>
  <p class="abs" style="left:150px;top:1388px;width:330px;font-size:11px;line-height:1.75">Every Ingredient Is Chosen With Intention — No Fillers, No Harsh Chemicals, Only Pure Plant-Based Actives That Work In Harmony With Your Skin.</p>
  <a class="btn btn-fill" style="left:150px;top:1485px;width:147px;height:36px">Discover More</a>
  <svg class="abs" style="left:620px;top:1285px" width="220" height="70" viewBox="0 0 220 70" fill="none" stroke="#9a9a92" stroke-width="1">
    <path d="M10 55 C40 -5 170 -5 210 60"/><path d="M5 48 L10 55 L17 50"/><path d="M204 56 L210 60 L212 52"/>
  </svg>
  <div class="photo" role="img" aria-label="Portrait of a woman touching cream under her eye" style="left:523px;top:1348px;width:235px;height:319px;border-radius:8px;background:linear-gradient(160deg,#e9ddd4 0%,#d9c5b6 60%,#c9b3a2 100%)"></div>
  <div class="photo" role="img" aria-label="Three Serapoise botanical balm jars" style="left:783px;top:1370px;width:267px;height:268px;border-radius:10px;background:linear-gradient(180deg,#f1f1ef,#e8e8e5)"></div>
  <div class="display abs" style="left:783px;top:1650px;font-size:19px">Botanical Balm</div>
  <div class="abs" style="left:1006px;top:1652px;font-size:13px;font-weight:500"><span style="color:var(--star)">★</span> 4.8</div>
</section>

<!-- STORY -->
<section class="story">
  <div class="photo" role="img" aria-label="Glass dropper bottles arranged among smooth white stones in black and white" style="left:0;top:0;width:593px;height:562px;background:linear-gradient(135deg,#9e9e9e 0%,#cfcfcf 45%,#b4b4b4 100%)"></div>
</section>
<h2 class="display abs" style="left:655px;top:1795px;font-size:54px;color:var(--accent-soft)">Our Story</h2>
<p class="abs" style="left:655px;top:1885px;width:400px;font-size:10.5px;line-height:1.8;padding-left:18px;border-left:2px solid var(--accent)">Lorem Ipsum Dolor Sit Amet Consectetur. Dolor Tortor Cursus Odio Volutpat Est Nisl. Pharetra In Mattis Morbi Amet. Leo Quis Suspendisse Nunc Egestas Volutpat Sed Lectus Ac. Lobortis Nunc Tincidunt Pretium Maecenas Diam Id Diam Nam.</p>
<p class="bullet" style="left:672px;top:1982px;width:400px;font-size:12px;color:var(--ink)">Lorem Ipsum Dolor Sit Amet Consectetur. Quis Dolor Lorem Mauris Ut Integer Eget Hac. Id Non Ornare Sapien.</p>
<p class="bullet" style="left:672px;top:2035px;width:400px;font-size:12px;color:var(--ink)">Lorem Ipsum Dolor Sit Amet Consectetur. Elementum Ut Fermentum Tincidunt Mus Vestibulum Viverra. Interdum.</p>
<div class="stat" style="left:655px"><strong>11K</strong>Lorem Ipsum Dolor<br>Sit Amet</div>
<div class="stat" style="left:790px;padding-left:16px;border-left:1px solid var(--accent)"><strong>10K</strong>Lorem Ipsum Dolor<br>Sit Amet</div>
<div class="stat" style="left:940px;padding-left:16px;border-left:1px solid var(--accent)"><strong>15K</strong>Lorem Ipsum<br>Dolor Sit</div>
<a class="btn btn-fill" style="left:655px;top:2235px;width:153px;height:38px">Read Our Story</a>

<!-- VALUES -->
<h2 class="display abs" style="left:0;top:2405px;width:1200px;text-align:center;font-size:54px">Our Product Are</h2>
<div class="value" style="left:127px">
  <svg width="54" height="54" viewBox="0 0 54 54" fill="none" stroke="#1f1f1f" stroke-width="1.4"><circle cx="27" cy="27" r="24"/><circle cx="27" cy="27" r="11"/><path d="M19 35 L35 19"/></svg>Cruelty Free</div>
<div class="value" style="left:282px">
  <svg width="54" height="54" viewBox="0 0 54 54" fill="none" stroke="#1f1f1f" stroke-width="1.4"><path d="M20 8 h12 v8 l6 28 h-24 l6-28z"/><path d="M14 44 L40 20"/></svg>Sulfate Free</div>
<div class="value" style="left:445px">
  <svg width="54" height="54" viewBox="0 0 54 54" fill="none" stroke="#1f1f1f" stroke-width="1.4"><rect x="14" y="22" width="22" height="10" rx="2" transform="rotate(-40 25 27)"/><path d="M8 46 L16 38"/><path d="M34 14 L42 8"/><rect x="38" y="28" width="10" height="18" rx="2"/></svg>Hormone Free</div>
<div class="value" style="left:638px">
  <svg width="54" height="54" viewBox="0 0 54 54" fill="none" stroke="#1f1f1f" stroke-width="1.4"><rect x="6" y="17" width="42" height="20" rx="10"/><path d="M27 17 v20"/></svg>Drug Precursor Free</div>
<div class="value" style="left:802px">
  <svg width="54" height="54" viewBox="0 0 54 54" fill="none" stroke="#1f1f1f" stroke-width="1.4"><path d="M10 10 C14 26 20 38 27 48 C32 36 40 22 46 12"/><path d="M27 48 C26 36 30 24 38 16"/></svg>Vegan</div>
<div class="value" style="left:925px">
  <svg width="54" height="54" viewBox="0 0 54 54" fill="none" stroke="#1f1f1f" stroke-width="1.4"><rect x="10" y="10" width="14" height="22" rx="3" transform="rotate(-40 17 21)"/><path d="M32 32 q4 6 0 10 q-4-4 0-10z"/></svg>Dye Free</div>

<!-- SHOP -->
<h2 class="display abs" style="left:0;top:2685px;width:1200px;text-align:center;font-size:54px">Our Shop &amp; Procuts</h2>
<div class="card-img" role="img" aria-label="Grey Lumivelt botanical serum dropper bottle" style="left:226px"></div>
<div class="card-img" role="img" aria-label="White Serapoise botanical balm jar" style="left:609px"></div>
<div class="card-name" style="left:226px">PRODUCT NAME</div>
<div class="card-name" style="left:609px">PRODUCT NAME</div>
<p class="card-desc" style="left:226px">Lorem ipsum dolor sit amet consectetur. Sit bibendum mattis sed consectetur iaculis consectetur odio ac purus.</p>
<p class="card-desc" style="left:609px">Lorem ipsum dolor sit amet consectetur. Sit bibendum mattis sed consectetur iaculis consectetur odio ac purus.</p>
<div class="price" style="left:226px">$120<s>$220</s></div>
<div class="price" style="left:609px">$120<s>$220</s></div>
<div class="stars" style="left:510px">★★★★★</div>
<div class="stars" style="left:893px">★★★★★</div>
<a class="btn btn-fill" style="left:226px;top:3415px;width:306px;height:37px">Read More Info About</a>
<a class="btn btn-line" style="left:609px;top:3415px;width:306px;height:37px;color:var(--muted)">Read More Info About</a>
<div class="cart" style="left:548px"><svg width="18" height="16" viewBox="0 0 18 16" fill="none" stroke="#1f1f1f" stroke-width="1.3"><path d="M1 1h3l2 9h9l2-6H5"/><circle cx="7" cy="14" r="1.2"/><circle cx="14" cy="14" r="1.2"/></svg></div>
<div class="cart" style="left:931px"><svg width="18" height="16" viewBox="0 0 18 16" fill="none" stroke="#1f1f1f" stroke-width="1.3"><path d="M1 1h3l2 9h9l2-6H5"/><circle cx="7" cy="14" r="1.2"/><circle cx="14" cy="14" r="1.2"/></svg></div>

<!-- TESTIMONIALS -->
<h2 class="display abs" style="left:0;top:3528px;width:1200px;text-align:center;font-size:56px;line-height:1.08">Loved By<br>Thousands, Backed By Results</h2>
<article class="quote" style="left:97px"><div class="mark">“</div><p>This balm melted into my skin overnight. Texture is light, scent is calm, and my redness faded within a week. I now reach for it every morning.</p><div class="mark end">”</div><div class="who"><span class="avatar"></span>— MARA LIND</div></article>
<article class="quote" style="left:304px"><div class="mark">“</div><p>This balm melted into my skin overnight. Texture is light, scent is calm, and my redness faded within a week. I now reach for it every morning.</p><div class="mark end">”</div><div class="who"><span class="avatar"></span>— MARA LIND</div></article>
<article class="quote featured" style="left:504px"><div class="mark">“</div><p>This balm melted into my skin overnight. Texture is light, scent is calm, and my redness faded within a week. I now reach for it every morning.</p><div class="mark end">”</div><div class="who"><span class="avatar"></span>— Mara Lind</div></article>
<article class="quote" style="left:711px"><div class="mark">“</div><p>This balm melted into my skin overnight. Texture is light, scent is calm, and my redness faded within a week. I now reach for it every morning.</p><div class="mark end">”</div><div class="who"><span class="avatar"></span>— MARA LIND</div></article>
<article class="quote" style="left:918px"><div class="mark">“</div><p>This balm melted into my skin overnight. Texture is light, scent is calm, and my redness faded within a week. I now reach for it every morning.</p><div class="mark end">”</div><div class="who"><span class="avatar"></span>— MARA LIND</div></article>

<!-- FOOTER -->
<footer class="footer"></footer>
<div class="logo" style="left:150px;top:4180px;font-size:46px;color:var(--accent);letter-spacing:1px">DEW HARBOR</div>
<span class="social" style="left:152px"></span>
<span class="social" style="left:193px"></span>
<span class="social" style="left:234px"></span>
<span class="social" style="left:275px"></span>
<div class="abs" style="left:552px;top:4124px;font-size:16px">Get In Touch!</div>
<div class="abs" style="left:727px;top:4113px;width:316px;height:38px;background:#fff;border-radius:20px;font-size:10px;color:var(--muted);padding:13px 0 0 14px">Enter your email</div>
<a class="btn btn-fill" style="left:927px;top:4113px;width:116px;height:38px">Subscribe</a>
<div class="foot-col" style="left:552px"><h4>Contact</h4><ul>
  <li><svg width="10" height="12" viewBox="0 0 10 12" fill="none" stroke="#6b6b6b"><path d="M5 11 C1 6 1 4 1 4 a4 4 0 0 1 8 0 c0 0 0 2-4 7z"/><circle cx="5" cy="4" r="1.3"/></svg>14 Linden Quay, Harbor Row</li>
  <li><svg width="11" height="11" viewBox="0 0 11 11" fill="none" stroke="#6b6b6b"><path d="M2 1h2l1 3-1.5 1a6 6 0 0 0 2.5 2.5L7 6l3 1v2a1 1 0 0 1-1 1A8 8 0 0 1 1 2a1 1 0 0 1 1-1z"/></svg>(000) 410-2276</li>
  <li><svg width="12" height="9" viewBox="0 0 12 9" fill="none" stroke="#6b6b6b"><rect x=".5" y=".5" width="11" height="8"/><path d="M.5 .5 6 5l5.5-4.5"/></svg>hello@dewharbor.test</li>
</ul></div>
<div class="foot-col" style="left:834px"><h4>Quick Link</h4><ul><li style="color:var(--ink)">Home</li><li>Our Story</li><li>Shop</li><li>FAQ</li><li>Blog</li></ul></div>
<div class="foot-col" style="left:985px"><h4>Useful</h4><ul style="margin-top:22px"><li style="color:var(--ink)">Privacy Policy</li><li style="color:var(--ink)">Legal</li><li style="color:var(--ink)">Terms Of Use</li><li style="color:var(--ink)">Cookie Policy</li></ul></div>
<div class="abs" style="left:150px;top:4378px;width:900px;height:1px;background:var(--accent-soft)"></div>
<div class="abs" style="left:0;top:4400px;width:1200px;text-align:center;font-size:9.5px">Copyright © 2025 All Rights Reserved.</div>

</body>
</html>
```